Flyer for Merchant Capital Cash Advance business

Need Flyer Design to be advertised on Social Media Platforms and also Print it to Publish it in Magazines.
Flyer Will be printed in different sizes for different publications.
Size 1) 6.25 inches * 11 inches.
Size 2) 8 inch * 11 inch
Size 3) 8 inch * 5.5 I inch
Size 4) 5 inch * 7 inch.
Google “Merchant Capital Cash advance flyer pics” to get an idea.

Flyer Design for Merchant Cash advance business.

Merchant Cash Advance is alternate to bank loans and does not require Personal Guarantee or Collateral.

Target Market(s)

Business owners seeking loan.

Industry/Entity Type

Business Service

Font styles to use
Serif
Sans Serif
Decorative
Script

Colors

Designer to choose colors to be used in the design.

Requirements
Must have
• Content from the Files Uploaded.
• Sharp Colors.
Nice to have
• Would like to see flyer in shape of a Bank Check or a $100 Bill.
• Would like to show a Comparison between Bank Loan and MCA.
• Open to any other ideas.

```html
<!DOCTYPE html>
<html lang="en">
<head>
<meta charset="UTF-8">
<title>Business Capital Cash Advance Flyer</title>
<link rel="stylesheet" href="https://fonts.googleapis.com/css2?family=Bebas+Neue&family=Oswald:wght@300&family=Nunito+Sans:ital,wght@0,400;0,600;1,400&display=swap">
<style>
  :root {
    --backdrop: #ececec;
    --photo-deep: #2f7f9c;
    --photo-light: #5bb6cc;
    --violet: #3e2a83;
    --sky: #3cbce8;
    --ink: #2b2b33;
    --slate: #414b55;
    --paper: #ffffff;
  }
  * { margin: 0; padding: 0; box-sizing: border-box; }
  html, body { width: 1200px; height: 1000px; overflow: hidden; }
  body { background: var(--backdrop); position: relative; font-family: "Nunito Sans", Arial, sans-serif; }

  .flyer {
    position: absolute; left: 266px; top: 25px;
    width: 688px; height: 947px; background: var(--paper); overflow: hidden;
  }

  .hero {
    position: absolute; left: 0; top: 0; width: 688px; height: 373px;
    background: linear-gradient(135deg, var(--photo-light) 0%, var(--photo-deep) 55%, #3f95b0 100%);
  }
  .hero-title {
    position: absolute; left: 0; top: 48px; width: 100%;
    text-align: center; color: #f4f7f8;
    font-family: "Bebas Neue", Impact, sans-serif;
    font-size: 101px; line-height: 88px; letter-spacing: 1px;
    -webkit-text-stroke: 1.5px #1f5f78;
  }

  .benefits {
    position: absolute; left: 0; top: 373px; width: 688px; height: 215px;
    background: var(--violet);
  }
  .notch { position: absolute; left: 309px; width: 70px; height: 37px; z-index: 2; }
  .notch-hero { top: 373px; }
  .notch-benefits { top: 588px; }
  .notch-pitch { top: 852px; }

  .benefit {
    position: absolute; display: flex; align-items: center; gap: 9px;
    color: #fff; font-style: italic; font-size: 17.5px; letter-spacing: 0.3px;
    text-transform: uppercase; white-space: nowrap;
  }
  .benefit svg { width: 26px; height: 26px; flex: none; }

  .pitch { position: absolute; left: 0; top: 588px; width: 688px; height: 264px; }
  .application-note {
    position: absolute; left: 147px; top: 80px; width: 388px; height: 44px;
    border-top: 1.5px solid var(--ink); border-bottom: 1.5px solid var(--ink);
    text-align: center; font-style: italic; font-size: 25px; line-height: 41px;
    color: var(--ink); letter-spacing: 0.5px;
  }
  .offer-line {
    position: absolute; left: 0; width: 100%; text-align: center;
    font-size: 41px; line-height: 44px; white-space: nowrap; color: var(--ink);
  }
  .offer-line.primary { top: 155px; }
  .offer-line.secondary { top: 205px; }
  .light { font-family: "Oswald", Arial, sans-serif; font-weight: 300; font-size: 37px; }
  .strong { font-family: "Bebas Neue", Impact, sans-serif; color: var(--violet); letter-spacing: 0.5px; }
  .accent { font-family: "Bebas Neue", Impact, sans-serif; color: var(--sky); font-style: italic; letter-spacing: 0.5px; }

  .contact-bar {
    position: absolute; left: 0; top: 852px; width: 688px; height: 95px;
    background: var(--slate); color: #fff;
  }
  .contact {
    position: absolute; left: 34px; display: flex; align-items: center; gap: 12px;
    font-size: 21px;
  }
  .contact svg { width: 24px; height: 24px; }
  .contact.phone { top: 14px; }
  .contact.email { top: 45px; }
  .business-name {
    position: absolute; right: 52px; top: 32px;
    font-size: 22px; font-weight: 600; letter-spacing: 0.8px;
  }
</style>
</head>
<body>
  <main class="flyer">
    <section class="hero" role="img" aria-label="Teal-tinted photo of a person holding a fan of hundred-dollar bills">
      <h1 class="hero-title">Say Hello<br>To A Better<br>Way To Borrow.</h1>
    </section>

    <svg class="notch notch-hero" viewBox="0 0 70 37"><polygon points="0,0 70,0 35,37" fill="#3f8da8"/></svg>

    <section class="benefits">
      <div class="benefit" style="left:52px; top:86px;">
        <svg viewBox="0 0 26 26"><circle cx="12" cy="14" r="10" fill="none" stroke="#3cbce8" stroke-width="2.4"/><path d="M7 14 L11.5 18.5 L23 3" fill="none" stroke="#3cbce8" stroke-width="3" stroke-linecap="round"/></svg>
        No Personal Guarantee
      </div>
      <div class="benefit" style="left:371px; top:86px;">
        <svg viewBox="0 0 26 26"><circle cx="12" cy="14" r="10" fill="none" stroke="#3cbce8" stroke-width="2.4"/><path d="M7 14 L11.5 18.5 L23 3" fill="none" stroke="#3cbce8" stroke-width="3" stroke-linecap="round"/></svg>
        No Guarantors Needed
      </div>
      <div class="benefit" style="left:52px; top:129px;">
        <svg viewBox="0 0 26 26"><circle cx="12" cy="14" r="10" fill="none" stroke="#3cbce8" stroke-width="2.4"/><path d="M7 14 L11.5 18.5 L23 3" fill="none" stroke="#3cbce8" stroke-width="3" stroke-linecap="round"/></svg>
        No Minimum Credit Score
      </div>
      <div class="benefit" style="left:371px; top:129px;">
        <svg viewBox="0 0 26 26"><circle cx="12" cy="14" r="10" fill="none" stroke="#3cbce8" stroke-width="2.4"/><path d="M7 14 L11.5 18.5 L23 3" fill="none" stroke="#3cbce8" stroke-width="3" stroke-linecap="round"/></svg>
        No Collateral Needed
      </div>
      <div class="benefit" style="left:247px; top:173px;">
        <svg viewBox="0 0 26 26"><circle cx="12" cy="14" r="10" fill="none" stroke="#3cbce8" stroke-width="2.4"/><path d="M7 14 L11.5 18.5 L23 3" fill="none" stroke="#3cbce8" stroke-width="3" stroke-linecap="round"/></svg>
        Bankruptcy – OK
      </div>
    </section>

    <svg class="notch notch-benefits" viewBox="0 0 70 37"><polygon points="0,0 70,0 35,37" fill="#3e2a83"/></svg>

    <section class="pitch">
      <p class="application-note">Simple One Page Application.</p>
      <p class="offer-line primary"><span class="light">GET </span><span class="strong">Business Capital Cash Advance</span></p>
      <p class="offer-line secondary"><span class="light">A </span><span class="accent">Convenient Alternative </span><span class="light">TO BANK LOAN.</span></p>
    </section>

    <footer class="contact-bar">
      <div class="contact phone">
        <svg viewBox="0 0 24 24"><path d="M6.5 2.5 L9.5 7 L7.5 9 C8.5 11.5 10.5 14 13 15.5 L15 13.5 L19.5 16.5 L17.5 20.5 C11 20 4 13 3.5 6.5 Z" fill="#fff"/></svg>
        (123) 456.7890
      </div>
      <div class="contact email">
        <svg viewBox="0 0 24 24"><rect x="1.5" y="5" width="21" height="14" fill="none" stroke="#fff" stroke-width="2"/><path d="M1.5 5 L12 13 L22.5 5" fill="none" stroke="#fff" stroke-width="2"/></svg>
        info@business.com
      </div>
      <div class="business-name">BUSINESS NAME</div>
    </footer>

    <svg class="notch notch-pitch" viewBox="0 0 70 37"><polygon points="0,0 70,0 35,37" fill="#ffffff"/></svg>
  </main>
</body>
</html>
```